Olive Oil bottle label front and back

We need a label designed for an olive oil bottle along with a company logo. I have attached the bottle and the exact design of the bottle.

Our company is called Veronel Amber Imports LLC but our olive oil will be called Veronel Amber

Front - as you are looking at the bottle the handle will be to the right

Our logo
Kalamata Protected Designation of Origin stamp - if you can not find this leave a spot for it and the factory can add it
ISO certified protected designated Origin stamp - if you can not find this leave a spot for it and the factory can add it
Look Greek, simple, elegant
Look expensive
What type of oil - extra virgin, organic.

Back

Greek flag
Nutrition facts
Bar code just leave a white space for this
Website http://veronelamberimports.com
Factory info - Kalamata, Greece
Best by date/made on date
Leave a space for company address

This link takes you to the bottle maker http://www.dortenvessel.gr/en/proionta/ladi-ksidi/item/807-10300

Target Market(s)

We are going to be starting to sell to upscale grocery stores and specialty food stores.

Industry/Entity Type

Food Production

Requirements
Must have
• Have gold in it because of the name and logo but not shinny, old fashioned looking gold. We want more of that simple elegant looking gold.

```html
<!DOCTYPE html>
<html lang="en">
<head>
<meta charset="utf-8">
<title>Veronel Amber Olive Oil – Front and Back Label</title>
<link rel="stylesheet" href="https://fonts.googleapis.com/css2?family=Cinzel+Decorative:wght@700&family=Source+Sans+3:wght@400;600;700;800&family=Archivo+Narrow:wght@400;700&display=swap">
<style>
  :root {
    --paper: #ffffff;
    --outline: #2b2b2b;
    --label: #1f2a1c;
    --label-pattern: #2c3d26;
    --gold: #e3c22b;
    --ink: #111111;
    --white: #ffffff;
    --flag-blue: #1f5fb4;
  }
  * { margin: 0; padding: 0; box-sizing: border-box; }
  html, body { width: 1200px; height: 1000px; overflow: hidden; background: var(--paper); }
  .canvas { position: relative; width: 1200px; height: 1000px; font-family: "Source Sans 3", sans-serif; }
  .bottles { position: absolute; inset: 0; }
  .bottle-line { fill: var(--paper); stroke: var(--outline); stroke-width: 1.3; }
  .cap-line { fill: none; stroke: var(--outline); stroke-width: 1; }
  .label-shape { fill: var(--label); }

  .abs { position: absolute; }
  .center { text-align: center; }

  /* Front label */
  .front-kind { left: 285px; width: 215px; color: var(--gold); font-weight: 700; font-size: 21px; line-height: 28px; letter-spacing: .5px; }
  .front-title { left: 285px; width: 215px; color: var(--gold); font-family: "Cinzel Decorative", serif; font-weight: 700; font-size: 44px; line-height: 50px; }
  .olive-branch { left: 330px; top: 588px; width: 115px; height: 90px; background: radial-gradient(ellipse at center, #6b5f20 0%, #3b3a1e 70%, transparent 72%); }
  .brand-name { left: 285px; width: 215px; color: var(--gold); font-weight: 700; font-size: 34px; line-height: 36px; }

  /* Back label */
  .back-kind { left: 700px; width: 215px; top: 398px; color: var(--gold); font-weight: 700; font-size: 16px; line-height: 16.5px; letter-spacing: .4px; }
  .origin { left: 700px; width: 215px; top: 448px; color: var(--white); font-size: 18px; line-height: 22px; }
  .flag { left: 733px; top: 474px; width: 45px; height: 28px; }
  .importer { left: 712px; top: 506px; width: 88px; color: var(--gold); }
  .importer-name { font-weight: 700; font-size: 15px; line-height: 16px; }
  .importer-detail { font-family: "Archivo Narrow", sans-serif; font-size: 8px; line-height: 12.5px; margin-top: 4px; }
  .story { left: 802px; top: 472px; width: 106px; color: var(--white); font-family: "Archivo Narrow", sans-serif; font-size: 8.6px; line-height: 13.6px; }

  .nutrition { left: 746px; top: 604px; width: 124px; height: 175px; background: var(--white); padding: 3px 4px; color: var(--ink); font-family: Arial, "Source Sans 3", sans-serif; font-size: 5.6px; line-height: 6.4px; }
  .nf-title { font-weight: 800; font-size: 14px; line-height: 13px; }
  .nf-rule-thick { border-top: 5px solid var(--ink); margin: 2px 0 1px; }
  .nf-rule-mid { border-top: 2.5px solid var(--ink); margin: 1px 0; }
  .nf-row { display: flex; justify-content: space-between; border-top: .5px solid var(--ink); }
  .nf-row.indent span:first-child { padding-left: 5px; }
  .nf-row b { font-weight: 800; }
  .nf-note { margin-top: 2px; font-size: 4.6px; line-height: 5.4px; }

  .code-space { left: 746px; top: 788px; width: 124px; height: 66px; background: var(--white); }
  .best-by { position: absolute; left: 5px; bottom: 5px; font-family: "Archivo Narrow", sans-serif; font-size: 8px; color: var(--ink); }
</style>
</head>
<body>
<div class="canvas">

  <svg class="bottles" width="1200" height="1000" viewBox="0 0 1200 1000">
    <defs>
      <g id="bottle-outline">
        <path class="bottle-line" d="M343 55 L343 130 C343 200 300 240 290 300 C277 360 275 420 275 480 L290 935 C290 960 265 965 265 987 L517 987 C517 965 493 960 493 935 L508 480 C508 420 505 360 515 320 C535 280 542 240 538 200 C535 150 500 120 470 120 L432 118 L432 55 Z"/>
        <path class="bottle-line" d="M445 160 C452 146 480 150 485 175 C490 220 490 262 478 274 C468 280 450 250 442 220 C438 200 440 176 445 160 Z"/>
        <path class="bottle-line" d="M335 55 L335 22 C335 12 338 6 346 5 L429 5 C437 6 440 12 440 22 L440 55 Z"/>
        <path class="cap-line" d="M335 40 L440 40 M340 14 L346 5 M350 14 L356 5 M360 14 L366 5 M420 14 L426 5 M430 14 L436 5"/>
      </g>
    </defs>

    <!-- Front bottle, handle on the right -->
    <use href="#bottle-outline"/>
    <path class="label-shape" role="img" aria-label="Dark green label with faint Greek key band pattern"
          d="M285 872 L285 440 C285 392 340 378 392 378 C445 378 500 392 500 440 L500 872 Z"/>

    <!-- Back bottle, handle on the left -->
    <g transform="matrix(-1 0 0 1 1211 0)">
      <use href="#bottle-outline"/>
    </g>
    <path class="label-shape" d="M700 870 L700 442 C700 396 752 384 807 384 C862 384 915 396 915 442 L915 870 Z"/>
  </svg>

  <!-- Front label text -->
  <div class="abs center front-kind" style="top:427px">ORGANIC<br>EXTRA VIRGIN</div>
  <div class="abs center front-title" style="top:478px">OLIVE<br>OIL</div>
  <div class="abs olive-branch" role="img" aria-label="Gold line drawing of an olive branch with olives"></div>
  <div class="abs center brand-name" style="top:694px">Veronel<br>Amber</div>

  <!-- Back label -->
  <div class="abs center back-kind">ORGANIC<br>EXTRA VIRGIN<br>OLIVE OIL</div>
  <div class="abs center origin">Kalamata, Greece</div>

  <svg class="abs flag" viewBox="0 0 27 18" aria-label="Greek flag">
    <rect width="27" height="18" fill="var(--white)"/>
    <g fill="var(--flag-blue)">
      <rect y="0" width="27" height="2"/>
      <rect y="4" width="27" height="2"/>
      <rect y="8" width="27" height="2"/>
      <rect y="12" width="27" height="2"/>
      <rect y="16" width="27" height="2"/>
      <rect width="10" height="10"/>
    </g>
    <rect x="4" width="2" height="10" fill="var(--white)"/>
    <rect y="4" width="10" height="2" fill="var(--white)"/>
  </svg>

  <div class="abs center importer">
    <div class="importer-name">Veronel Amber Imports LLC</div>
    <div class="importer-detail">Street Address line 1<br>City Address line 2<br>veronelamberimports.com</div>
  </div>

  <p class="abs story">Lorem ipsum dolor sit amet, consectetuer adipiscing elit, sed diam nonummy nibh euismod . Lorem ipsum dolor sit amet, consectetuer adipiscing elit, sed diam nonummy nibh euismod . Lorem ipsum dolor sit amet, consectetuer adipiscing elit, sed diameuismod.</p>

  <div class="abs nutrition">
    <div class="nf-title">Nutrition Facts</div>
    <div>Serving Size 1 Tbsp (15 ml)</div>
    <div>Servings Per Container 200</div>
    <div class="nf-rule-thick"></div>
    <div><b>Amount Per Serving</b></div>
    <div class="nf-row"><span><b>Calories</b> 120</span><span><b>Fat Cal</b> 120</span></div>
    <div class="nf-rule-mid"></div>
    <div class="nf-row" style="justify-content:flex-end"><span><b>%Daily Value*</b></span></div>
    <div class="nf-row"><span><b>Total Fat</b> 14g</span><b>22%</b></div>
    <div class="nf-row indent"><span>Saturated Fat 2g</span><b>10%</b></div>
    <div class="nf-row indent"><span>Trans Fat 0g</span><b>0%</b></div>
    <div class="nf-row indent"><span>Polyunsaturated Fat 1.6g</span><b>0%</b></div>
    <div class="nf-row indent"><span>Monounsaturated Fat 10.4g</span><b>0%</b></div>
    <div class="nf-row"><span><b>Cholesterol</b> 0mg</span><b>0%</b></div>
    <div class="nf-row"><span><b>Sodium</b> 0mg</span><b>0%</b></div>
    <div class="nf-row"><span><b>Total Carbohydrate</b> 0g</span><b>0%</b></div>
    <div class="nf-row"><span><b>Protein</b> 0g</span><b>0%</b></div>
    <div class="nf-rule-thick"></div>
    <div class="nf-note">Not a significant source of dietary fiber, sugars, vitamin A, vitamin C, calcium and iron.</div>
    <div class="nf-note">*Percent Daily values are based on a 2000 calories diet.</div>
  </div>

  <div class="abs code-space">
    <span class="best-by">BEST BY DATE:</span>
  </div>

</div>
</body>
</html>
```